Business Card Design

We need a business card design for our new expansion based in Bloomfield Hills, Michigan. Our company is Quiet Harbor Institute & Wellness Center. Our Academy teaches individuals of all ages and professions to live from their soul. We teach intuitive development, meditation and mindfulness; shamanic healing. And ourr healing center provides holistic services. We offer certification programs that support the ethical practices of Intuitive professionals. Our team of Intuitive Practitioners includes: doctors, psychologists, chiropractor, soul retrievers, mediums, etc who all balance their knowledge with intuitive wisdom.

We want our symbol to be the Blue Morpho Buttefly and the colors on the card to complement it. We want to communicate inspiration, healing and empowerment. Thank you
Updates

Industry/Entity Type

Business

Contact Information for Business Card

Dana Orwick
Medium. Author. Soul Retriever.
Founder, Quiet Harbor

Quiet Harbor

19 North Cedar Mill Drive Suite 100
Fernwood Heights, MI 48517
248-603-7418

www.danaorwick.example

Requirements
Must have
• blue morpho butterfly

```html
<!DOCTYPE html>
<html lang="en">
<head>
<meta charset="utf-8">
<title>Quiet Harbor Business Card</title>
<link rel="stylesheet" href="https://fonts.googleapis.com/css2?family=Exo+2:wght@400;500;600&display=swap">
<style>
  :root {
    --page-bg: #e4e4e2;
    --card-dark: #2f2f31;
    --panel-blue: #1e86d6;
    --panel-blue-light: #2aa2ea;
    --panel-blue-deep: #1565b8;
    --edge-grey: #a9abae;
    --brand-blue: #4f86e0;
    --emblem-light: #35b5f0;
    --emblem-deep: #3d6fd6;
    --icon-blue: #3b8be0;
    --text-light: #f4f5f7;
  }
  * { margin: 0; padding: 0; box-sizing: border-box; }
  html, body {
    width: 1200px; height: 899px; overflow: hidden;
    background: var(--page-bg);
    font-family: "Exo 2", sans-serif;
  }
  .business-card {
    position: absolute; left: 100px; top: 163px;
    width: 1000px; height: 572px;
    background: var(--card-dark);
    overflow: hidden;
    box-shadow: 0 10px 30px rgba(0,0,0,0.25);
  }
  .side-panel { position: absolute; inset: 0; width: 1000px; height: 572px; }
  .brand {
    position: absolute; left: 120px; top: 70px; width: 340px;
    display: flex; flex-direction: column; align-items: center; gap: 14px;
  }
  .brand-emblem {
    width: 150px; height: 80px; border-radius: 40px;
    background: radial-gradient(circle at 50% 50%, var(--emblem-light), var(--emblem-deep));
  }
  .brand-name {
    color: var(--brand-blue);
    font-size: 36px; font-weight: 500;
    letter-spacing: 4px; text-transform: uppercase; white-space: nowrap;
  }
  .address {
    position: absolute; left: 120px; top: 262px;
    color: var(--text-light);
    font-size: 21px; line-height: 30px; letter-spacing: 1px;
  }
  .contact-list {
    position: absolute; left: 120px; top: 350px;
    list-style: none;
  }
  .contact-item {
    display: flex; align-items: center; gap: 16px;
    color: var(--text-light);
    font-size: 19px; line-height: 38px; letter-spacing: 1px;
  }
  .contact-icon { width: 20px; height: 20px; fill: var(--icon-blue); flex: none; }
  .person {
    position: absolute; left: 735px; top: 245px; width: 265px;
    text-align: center; color: var(--text-light); text-transform: uppercase;
  }
  .person-name { font-size: 26px; font-weight: 600; letter-spacing: 1px; }
  .person-title { font-size: 14px; font-weight: 400; letter-spacing: 1px; margin-top: 6px; white-space: nowrap; }
</style>
</head>
<body>
<div class="business-card">
  <svg class="side-panel" viewBox="0 0 1000 572" aria-hidden="true">
    <defs>
      <radialGradient id="panelGlow" cx="0.55" cy="0.35" r="0.8">
        <stop offset="0" stop-color="#2aa2ea"/>
        <stop offset="0.6" stop-color="#1e86d6"/>
        <stop offset="1" stop-color="#1565b8"/>
      </radialGradient>
    </defs>
    <path d="M 750 0 C 672 150, 690 430, 838 572 L 1000 572 L 1000 0 Z" fill="#a9abae"/>
    <path d="M 762 0 C 686 150, 704 430, 852 572 L 1000 572 L 1000 0 Z" fill="url(#panelGlow)"/>
  </svg>

  <div class="brand">
    <div class="brand-emblem" role="img" aria-label="Blue morpho butterfly illustration"></div>
    <span class="brand-name">Quiet Harbor</span>
  </div>

  <p class="address">19 North Cedar Mill Drive Suite 100<br>Fernwood Heights, MI 48517</p>

  <ul class="contact-list">
    <li class="contact-item">
      <svg class="contact-icon" viewBox="0 0 24 24"><path d="M6.6 10.8a15.1 15.1 0 0 0 6.6 6.6l2.2-2.2a1 1 0 0 1 1-.25 11.4 11.4 0 0 0 3.6.57 1 1 0 0 1 1 1V20a1 1 0 0 1-1 1A17 17 0 0 1 3 4a1 1 0 0 1 1-1h3.5a1 1 0 0 1 1 1c0 1.25.2 2.45.57 3.57a1 1 0 0 1-.25 1z"/></svg>
      248-603-7418
    </li>
    <li class="contact-item">
      <svg class="contact-icon" viewBox="0 0 24 24"><path d="M7 1h10a2 2 0 0 1 2 2v18a2 2 0 0 1-2 2H7a2 2 0 0 1-2-2V3a2 2 0 0 1 2-2zm0 3v14h10V4zm5 15.2a1.2 1.2 0 1 0 0 2.4 1.2 1.2 0 0 0 0-2.4z"/></svg>
      248-603-7418
    </li>
    <li class="contact-item">
      <svg class="contact-icon" viewBox="0 0 24 24"><path d="M6 2h9l3 3v5H6zm-3 9h18a1 1 0 0 1 1 1v9a1 1 0 0 1-1 1H3a1 1 0 0 1-1-1v-9a1 1 0 0 1 1-1zm3 3v2h2v-2zm4 0v2h2v-2zm4 0v2h2v-2zm-8 4v2h2v-2zm4 0v2h2v-2zm4 0v2h2v-2z"/></svg>
      248-603-7418
    </li>
    <li class="contact-item">
      <svg class="contact-icon" viewBox="0 0 24 24"><path d="M2 5h20v14H2zm2 2v.5l8 5.5 8-5.5V7zm0 3v7h16v-7l-8 5.5z"/></svg>
      hello@quietharbor.example
    </li>
    <li class="contact-item">
      <svg class="contact-icon" viewBox="0 0 24 24"><path d="M12 2a10 10 0 1 0 0 20 10 10 0 0 0 0-20zm6.9 6h-2.9a15 15 0 0 0-1.3-3.7A8 8 0 0 1 18.9 8zM12 4c.8 1.1 1.5 2.5 1.9 4h-3.8c.4-1.5 1.1-2.9 1.9-4zM4.3 14a8 8 0 0 1 0-4h3.3a16 16 0 0 0 0 4zm.8 2h2.9a15 15 0 0 0 1.3 3.7A8 8 0 0 1 5.1 16zM8 8H5.1a8 8 0 0 1 4.2-3.7A15 15 0 0 0 8 8zm4 12c-.8-1.1-1.5-2.5-1.9-4h3.8c-.4 1.5-1.1 2.9-1.9 4zm2.3-6H9.7a14 14 0 0 1 0-4h4.6a14 14 0 0 1 0 4zm.4 5.7A15 15 0 0 0 16 16h2.9a8 8 0 0 1-4.2 3.7zm1.7-5.7a16 16 0 0 0 0-4h3.3a8 8 0 0 1 0 4z"/></svg>
      www.danaorwick.example
    </li>
  </ul>

  <div class="person">
    <p class="person-name">Dana Orwick</p>
    <p class="person-title">Medium. Author. Soul Retriever.</p>
  </div>
</div>
</body>
</html>
```